I want a business letter head designed, one that I can have printed but also one that I can use as an insert for proforma documentation that is printed in house.

Business name : RJ Pemberly & Associates
Address: PO Box 732
Coralbrook Qld 4871

Type of business: Accounting practice- accounting, taxation, audit, self managed superannuation,

Colour scheme: black and blue - previously designed a business card; however the blue that is one the cards is very washed out and I am not particularly happy with it.

```html
<!DOCTYPE html>
<html lang="en">
<head>
<meta charset="utf-8">
<title>RJ Pemberly &amp; Associates – Letterhead</title>
<link rel="stylesheet" href="https://fonts.googleapis.com/css2?family=Arimo:wght@400;700&family=Tinos:wght@400&display=swap">
<style>
  :root {
    --backdrop: #0aa2e4;
    --paper: #ffffff;
    --band: #000000;
    --brand-blue: #1a8fe6;
    --pale-blue: #b8defa;
    --ink: #111111;
    --on-band: #ffffff;
  }
  * { margin: 0; padding: 0; box-sizing: border-box; }
  html, body {
    width: 1200px;
    height: 1013px;
    overflow: hidden;
    background: var(--backdrop);
  }
  .letterhead {
    position: absolute;
    left: 263px;
    top: 26px;
    width: 674px;
    height: 960px;
    background: var(--paper);
    overflow: hidden;
  }
  .header-band {
    position: absolute;
    left: 0;
    top: 12px;
    width: 100%;
    height: 77px;
    background: var(--band);
  }
  .brand {
    position: absolute;
    left: 44px;
    top: 6px;
    display: flex;
    align-items: center;
    gap: 14px;
  }
  .brand-square {
    width: 64px;
    height: 64px;
    background: var(--brand-blue);
  }
  .brand-name {
    font-family: "Tinos", "Times New Roman", serif;
    font-weight: 400;
    font-size: 23px;
    line-height: 21px;
    color: var(--on-band);
  }
  .contact {
    position: absolute;
    right: 36px;
    top: 25px;
    text-align: right;
    font-family: "Arimo", Arial, sans-serif;
    font-size: 11.5px;
    line-height: 18px;
    color: var(--on-band);
  }
  .corner-accent {
    position: absolute;
    right: 0;
    bottom: 0;
    width: 222px;
    height: 208px;
    background: var(--pale-blue);
    opacity: 0.9;
  }
  .services {
    position: absolute;
    left: 47px;
    top: 933px;
    font-family: "Arimo", Arial, sans-serif;
    font-size: 11px;
    color: var(--ink);
    word-spacing: 1px;
  }
  .services span + span::before {
    content: " . ";
    margin-left: 6px;
  }
</style>
</head>
<body>
  <main class="letterhead">
    <header class="header-band">
      <div class="brand">
        <div class="brand-square"></div>
        <div class="brand-name">RJ Pemberly<br>&amp; Associates.</div>
      </div>
      <address class="contact" style="font-style:normal">
        P.O. Box 732 Coralbrook Qld 4871<br>
        email: jenna@rjpemberlyassociates.com.au
      </address>
    </header>

    <div class="corner-accent"></div>

    <footer class="services">
      <span>Accounting</span><span>Taxation</span><span>Audit</span><span>Self Managed</span><span>Superannuation</span>
    </footer>
  </main>
</body>
</html>
```